Velora Aesthetica

Medical doctor providing aesthetic medicine

* Double sided card
* Logo to be on card
Other details:
* Dr. Mirela Kostvan, BSc, MBChB, CCFP
* #214-215, 27903 83 Ave, Surrey, BC, V2T 4K7
* 604-718-2943
* info@veloraclinic.ca
* www.veloraclinic.ca

Industry/Entity Type

Medical / Health & Beauty

Contact Information for Business Card

see 'Project Description'

Colors
0054AA
0677BA
7BADD7
CADEEF
E8F1F8
FFF300
FFF600
FEFA6F
FFFEC7
FFFEE8

Requirements
Must have
• Modern, high-end design

```html
<!DOCTYPE html>
<html lang="en">
<head>
<meta charset="utf-8">
<title>Velora Aesthetica — Business Card</title>
<link rel="stylesheet" href="https://fonts.googleapis.com/css2?family=Montserrat:wght@600&family=Poppins:wght@400;600&display=swap">
<style>
  :root {
    --backdrop: #232323;
    --card-dark: #212124;
    --gold: #c9a13a;
    --gold-light: #e2bb2c;
    --gold-edge: #c5a03d;
    --gold-deep: #c7a233;
    --white: #ffffff;
    --text-soft: #ececec;
  }
  * { margin: 0; padding: 0; box-sizing: border-box; }
  html, body {
    width: 1200px; height: 711px; overflow: hidden;
    background: var(--backdrop);
  }
  .canvas { position: relative; width: 1200px; height: 711px; }

  .card {
    position: absolute; left: 341px; width: 519px; height: 296px;
    border-radius: 20px; overflow: hidden;
  }
  .card--front {
    top: 45px;
    background: linear-gradient(90deg, var(--gold-deep) 0%, var(--gold-light) 50%, var(--gold-deep) 100%);
  }
  .card--back {
    top: 370px;
    background: var(--card-dark);
    border: 1.5px solid var(--gold-edge);
  }

  .brand-name {
    font-family: "Montserrat", sans-serif; font-weight: 600;
    text-transform: uppercase; text-align: center; line-height: 1.35;
  }
  .card--front .brand-name {
    position: absolute; left: 0; right: 0; top: 112px;
    color: var(--white); font-size: 24px; letter-spacing: 8px;
  }
  .card--back .brand-name {
    position: absolute; left: 18px; width: 200px; top: 122px;
    color: var(--white); font-size: 17px; letter-spacing: 5px;
  }

  .divider {
    position: absolute; left: 258px; top: 58px;
    width: 1px; height: 179px; background: var(--gold);
  }

  .contact-block {
    position: absolute; left: 297px; top: 87px;
    font-family: "Poppins", sans-serif; color: var(--text-soft);
  }
  .person-name { font-size: 19.5px; line-height: 1.2; font-weight: 400; color: var(--white); }
  .person-name .given { font-weight: 600; color: var(--gold); }
  .credentials { font-size: 13px; margin-top: 2px; }
  .contact-list { list-style: none; margin-top: 22px; }
  .contact-list li {
    display: flex; align-items: center; gap: 7px;
    font-size: 13px; line-height: 16.5px;
  }
  .contact-list svg { width: 12px; height: 12px; flex: none; }

  .address {
    position: absolute; left: 0; right: 0; top: 259px;
    text-align: center; font-family: "Poppins", sans-serif;
    font-size: 13px; color: var(--gold);
  }
</style>
</head>
<body>
<main class="canvas">
  <section class="card card--front" aria-label="Card front">
    <p class="brand-name">Velora<br>Aesthetica</p>
  </section>

  <section class="card card--back" aria-label="Card back">
    <p class="brand-name">Velora<br>Aesthetica</p>
    <div class="divider"></div>
    <div class="contact-block">
      <h1 class="person-name"><span class="given">Dr. Mirela</span> Kostvan</h1>
      <p class="credentials">BSc, MBChB, CCFP</p>
      <ul class="contact-list">
        <li>
          <svg viewBox="0 0 24 24" aria-hidden="true"><path fill="#c9a13a" d="M6.6 10.8a15.1 15.1 0 0 0 6.6 6.6l2.2-2.2a1 1 0 0 1 1-.25 11.4 11.4 0 0 0 3.6.57 1 1 0 0 1 1 1V20a1 1 0 0 1-1 1A17 17 0 0 1 3 4a1 1 0 0 1 1-1h3.5a1 1 0 0 1 1 1c0 1.25.2 2.45.57 3.57a1 1 0 0 1-.25 1z"/></svg>
          604-718-2943
        </li>
        <li>
          <svg viewBox="0 0 24 24" aria-hidden="true"><rect x="2" y="5" width="20" height="14" rx="1.5" fill="none" stroke="#c9a13a" stroke-width="2"/><path d="M3 6l9 7 9-7" fill="none" stroke="#c9a13a" stroke-width="2"/></svg>
          info@veloraclinic.ca
        </li>
        <li>
          <svg viewBox="0 0 24 24" aria-hidden="true"><circle cx="12" cy="12" r="9.5" fill="none" stroke="#c9a13a" stroke-width="2"/><path d="M2.5 12h19M12 2.5c3 3 3 16 0 19M12 2.5c-3 3-3 16 0 19" fill="none" stroke="#c9a13a" stroke-width="1.6"/></svg>
          www.veloraclinic.ca
        </li>
      </ul>
    </div>
    <p class="address">#214-215, 27903 83 Ave, Surrey, BC, V2T 4K7</p>
  </section>
</main>
</body>
</html>
```